Keystone Gasket Works
Business cards and letter head
Project: Keystone Gasket Works
Keystone Gasket Works -
Creative Brief
Professional
Marwen Tolk
President
4818 Calloway Street Denver CO. 80219
marwen@keystone-gask.com
www.keystone-gask.com

```html
<!DOCTYPE html>
<html lang="en">
<head>
<meta charset="utf-8">
<title>Keystone Gasket Works — Stationery</title>
<link href="https://fonts.googleapis.com/css2?family=Roboto:wght@400;700;900&display=swap" rel="stylesheet">
<style>
:root{
  --bg:#ececec;
  --paper:#ffffff;
  --red:#d8232a;
  --dark:#1b1b1b;
  --ink:#333333;
  --muted:#777777;
  --shadow:0 2px 8px rgba(0,0,0,.18);
}
*{box-sizing:border-box;margin:0;padding:0}
html,body{width:1200px;height:751px;overflow:hidden;background:var(--bg);font-family:"Roboto",Arial,sans-serif;color:var(--ink)}
.canvas{position:relative;width:1200px;height:751px}
.sheet{position:absolute;background:var(--paper);box-shadow:var(--shadow)}
.brand{display:flex;align-items:center;gap:8px}
.brand-dot{border-radius:50%;background:var(--dark);flex:none}
.brand-name{font-weight:900;color:var(--red);text-transform:uppercase;line-height:1.05}
.swoosh{position:absolute}
.swoosh-red{background:radial-gradient(circle at 0 0,rgba(216,35,42,.85),rgba(216,35,42,0) 70%)}
.swoosh-dark{background:radial-gradient(circle at 0 100%,rgba(30,30,30,.8),rgba(30,30,30,0) 70%)}
.swoosh-dark-br{background:radial-gradient(circle at 100% 100%,rgba(30,30,30,.8),rgba(30,30,30,0) 70%)}
.small{font-size:8px;line-height:1.45}
.tiny{font-size:6.5px;line-height:1.5}

/* letterhead */
.letterhead{left:110px;top:58px;width:470px;height:650px}
.letterhead .brand{position:absolute;left:52px;top:36px}
.letterhead .brand-dot{width:36px;height:36px}
.letterhead .brand-name{font-size:22px;width:190px}
.letterhead .swoosh-red{left:0;top:0;width:90px;height:80px}
.letterhead .swoosh-dark{left:0;bottom:20px;width:120px;height:110px}
.letterhead .footer{position:absolute;left:130px;bottom:22px;font-size:8px;line-height:1.6}

/* envelopes */
.envelope-red{left:700px;top:70px;width:440px;height:200px;background:var(--red)}
.envelope-black{left:740px;top:120px;width:420px;height:210px;background:#2a2a2a}
.envelope{left:600px;top:120px;width:470px;height:230px}
.envelope .brand{position:absolute;left:40px;top:28px}
.envelope .brand-dot{width:26px;height:26px}
.envelope .brand-name{font-size:15px;width:170px}
.envelope .swoosh-dark-br{right:0;bottom:0;width:110px;height:90px}
.envelope .return{position:absolute;left:40px;bottom:26px}

/* cards */
.card{width:210px;height:120px}
.card-dark{background:var(--dark);color:#e6e6e6}
.card-dark-front{left:40px;top:300px}
.card-dark-back{left:40px;top:440px}
.card-light-front{left:600px;top:480px}
.card-light-back{left:835px;top:480px}
.card .brand{position:absolute;left:14px;top:12px}
.card .brand-dot{width:20px;height:20px}
.card-dark .brand-dot{background:#e6e6e6}
.card .brand-name{font-size:12px;width:140px}
.card .person{position:absolute;left:14px;top:62px}
.card .person strong{display:block;font-size:9px}
.card .contact{position:absolute;left:104px;top:62px;border-left:1px solid #999;padding-left:6px}
.card .swoosh{right:0;bottom:0;width:70px;height:60px}
.card-dark .swoosh{background:radial-gradient(circle at 100% 100%,rgba(230,230,230,.5),rgba(230,230,230,0) 70%)}
.card-back-mark{position:absolute;left:50%;top:50%;transform:translate(-50%,-60%);width:30px;height:30px;border-radius:50%}
.card-dark-back .card-back-mark{background:#e6e6e6}
.card-light-back .card-back-mark{background:var(--dark)}
.card-back-url{position:absolute;left:0;right:0;bottom:16px;text-align:center}
</style>
</head>
<body>
<main class="canvas">

  <section class="sheet letterhead">
    <div class="swoosh swoosh-red" role="img" aria-label="Red dashed arc decoration"></div>
    <div class="brand"><span class="brand-dot"></span><span class="brand-name">Keystone Gasket Works</span></div>
    <div class="swoosh swoosh-dark" role="img" aria-label="Dark dashed arc decoration"></div>
    <div class="footer">
      4818 Calloway Street Denver CO. 80219<br>
      <b>Phone:</b> (303) 555-0148 &nbsp;|&nbsp; <b>Fax:</b> (303) 555-0162<br>
      <b>Email:</b> marwen@keystone-gask.com &nbsp;|&nbsp; <b>Web:</b> www.keystone-gask.com
    </div>
  </section>

  <div class="sheet envelope-red" aria-hidden="true"></div>
  <div class="sheet envelope-black" aria-hidden="true"></div>
  <section class="sheet envelope">
    <div class="brand"><span class="brand-dot"></span><span class="brand-name">Keystone Gasket Works</span></div>
    <div class="return small">
      4818 Calloway Street Denver CO. 80219<br>
      Phone: (303) 555-0148 &nbsp;|&nbsp; Fax: (303) 555-0162<br>
      marwen@keystone-gask.com &nbsp;|&nbsp; www.keystone-gask.com
    </div>
    <div class="swoosh swoosh-dark-br" role="img" aria-label="Dark dashed arc decoration"></div>
  </section>

  <section class="sheet card card-dark card-dark-front">
    <div class="brand"><span class="brand-dot"></span><span class="brand-name">Keystone Gasket Works</span></div>
    <div class="person tiny"><strong>Marwen Tolk</strong>President</div>
    <div class="contact tiny">4818 Calloway Street<br>Denver CO. 80219<br>(303) 555-0148<br>marwen@keystone-gask.com</div>
    <div class="swoosh" role="img" aria-label="Dashed arc decoration"></div>
  </section>
  <section class="sheet card card-dark card-dark-back">
    <span class="card-back-mark"></span>
    <div class="card-back-url tiny">www.keystone-gask.com</div>
    <div class="swoosh" role="img" aria-label="Dashed arc decoration"></div>
  </section>

  <section class="sheet card card-light-front">
    <div class="brand"><span class="brand-dot"></span><span class="brand-name">Keystone Gasket Works</span></div>
    <div class="person tiny"><strong>Marwen Tolk</strong>President</div>
    <div class="contact tiny">4818 Calloway Street<br>Denver CO. 80219<br>(303) 555-0148<br>marwen@keystone-gask.com</div>
    <div class="swoosh swoosh-dark-br" role="img" aria-label="Dark dashed arc decoration"></div>
  </section>
  <section class="sheet card card-light-back">
    <span class="card-back-mark"></span>
    <div class="card-back-url tiny">www.keystone-gask.com</div>
    <div class="swoosh swoosh-dark-br" role="img" aria-label="Dark dashed arc decoration"></div>
  </section>

</main>
</body>
</html>
```